IT Company Business Card Design w/Stationary Design

We have a great logo we like! We are looking to redesign our business cards and all company logo'd merchandise/materials.

We are an IT Company located near the Bay Area (San Francisco, CA). We specialize in Managed Services and offer complete IT Computer and Network Support to Businesses of all sizes. We thrive on making a lasting impression. We have been doing IT for 15yrs+ but are young at heart. We like to stand out and be different. We want to be unique and have a recognizable brand. We need our logo to represent who we are. We are young, professional, creative and outstanding. We don't want to blend in, we want to stand out. Our business card needs to stand out and grab attention. Something Bold, yet simple and clean. (I will provide ideas of what we like to give a taste of what we are looking for).

The design can include any kind of texture/artistic design or sizing EXCEPT please "no square card designs" as they don't seem to fit in wallets very well. We dont mind curved edges, rounded corners, vertical layouts or horizontal layouts, embossing, letter press or raised surfaces. Again, we dont want to look average or plain or boring. :) Be creative - yet practical! We have ordered from Pebblecraft designs before and been very happy. Their card sizes tend to be a little different, so beware. Hope this helps!

Target Market(s)

Businesses - Small to Medium, Corporations, Publicly Traded Companies

Industry/Entity Type

Business

Contact Information for Business Card

Harbor Lantern IT
7318 Quillby Avenue
Suite F
Modesto, CA 95871

Office 209.555.0137
Direct 209.555.0182
Cell 209.555.0164

Ross Tavener
Founder, CEO
www.hlit-example.com
rtavener@hlit-example.com

Locations Serviced: Modesto, Stockton, Pleasanton, Fresno (incorporate this on the card ONLY if there's a good place to do so).

What we specialize in: Computer, Network, Voice, Data. (IT Services)

Our Logo Colors: Black and Blue (#006699). Open to using grey or orange as well - but not required. Don't want too busy....

Logo Font: "Cinthe" (Will attach logo font). We want type style to be clean. You can show different font types including our logo font - and we are open to other font ideas.

The logo can be separated. You can use elements together or apart. Surprise us! :) We "REALLY" want the "hl" to be our identifier/our brand people recognize.

Font styles to use
Sans Serif

Colors
0355a3
3176b5
f37122
f78f20
faa54b
474747
aaaaaa
757575
000000

Requirements
Must have
• Bold, Big, Colorful, Modern/yet Fun, Clean Design, Stand Out Presence, Texture would be welcomed - but not necessary, Card design shape can include cut corners or rounded or square edges. Be creative. (HOWEVER, we don't want a square design because we have found it doesn't fit in wallets that easily).
• We do like using Pebblecraft printing company (Which they have particular sizing on their card templates - beware), but are open to other design templates/printing companies as well. We just want to make sure its easy to find a print company to do our work. Too unique could be costly and hard to get cards printed.
• Colors to use: Our logo Blue (#006699), with either whites, grays, black, shades of our blue, and maybe a pinch of orange if needed. Primarily, blue, white, gray or black.
Nice to have
• Texture would be cool or little different edging or shape - but nothing too costly to print. I have seen cards with 3 sharp edges and one round edge. Something like that would be cool as an option. Or a vertical card.
• I love a faded watermark look. It would be nice to see some shading of our circle logo on a few designs. The circle with "hl" in it OR.... taking just the "hl" and using it alone.
Should not have
• No square card designs. Nothing too expensive or elaborate to print. No busy fonts. Do not like Times New Roman type fonts (too old looking). Not a lot of orange (if you even choose to use some orange).

```html
<!DOCTYPE html>
<html lang="en">
<head>
<meta charset="utf-8">
<title>Harbor Lantern IT – Business Card</title>
<link rel="stylesheet" href="https://fonts.googleapis.com/css2?family=Barlow:wght@400;500;600&display=swap">
<style>
  :root {
    --backdrop: #8e7b6e;
    --card-blue: #0b4f97;
    --emboss-blue: #07427f;
    --ink-white: #eef3fa;
    --rule-white: rgba(238, 243, 250, 0.85);
  }
  html, body {
    margin: 0;
    padding: 0;
    width: 1110px;
    height: 1200px;
    overflow: hidden;
    background: var(--backdrop);
    font-family: "Barlow", "Helvetica Neue", Arial, sans-serif;
  }
  .canvas {
    position: relative;
    width: 1110px;
    height: 1200px;
  }
  .card {
    position: absolute;
    left: 370px;
    width: 505px;
    height: 280px;
    background: var(--card-blue);
    overflow: hidden;
  }
  .card--front { top: 231px; }
  .card--back { top: 695px; }

  /* Front: brand name with a single plain circle */
  .brand {
    position: absolute;
    left: 0;
    right: 0;
    top: 56px;
    display: flex;
    flex-direction: column;
    align-items: center;
  }
  .brand__circle {
    width: 88px;
    height: 88px;
    border-radius: 50%;
    background: var(--emboss-blue);
  }
  .brand__name {
    margin-top: 22px;
    font-size: 36px;
    font-weight: 600;
    letter-spacing: 1px;
    color: var(--emboss-blue);
  }

  /* Back: contact details */
  .contact {
    position: absolute;
    left: 35px;
    top: 0;
    color: var(--ink-white);
  }
  .contact__name {
    position: absolute;
    top: 27px;
    margin: 0;
    font-size: 27px;
    font-weight: 500;
    letter-spacing: 0.5px;
    white-space: nowrap;
  }
  .contact__title {
    position: absolute;
    top: 60px;
    font-size: 16px;
    letter-spacing: 0.5px;
    white-space: nowrap;
  }
  .contact__rule {
    position: absolute;
    left: 0;
    width: 138px;
    height: 1px;
    background: var(--rule-white);
  }
  .contact__rule--top { top: 95px; }
  .contact__rule--bottom { top: 172px; }
  .phones {
    position: absolute;
    top: 108px;
    margin: 0;
    font-size: 13px;
    line-height: 17px;
    letter-spacing: 0.6px;
    display: grid;
    grid-template-columns: 57px auto;
    white-space: nowrap;
  }
  .phones dt, .phones dd { margin: 0; }
  .contact__line {
    position: absolute;
    font-size: 13px;
    letter-spacing: 0.4px;
    white-space: nowrap;
  }
  .contact__line--email { top: 186px; }
  .contact__line--email .label { display: inline-block; width: 57px; }
  .contact__line--address { top: 212px; }
  .contact__line--web { top: 242px; font-size: 14px; }
</style>
</head>
<body>
<main class="canvas">
  <section class="card card--front" aria-label="Card front">
    <div class="brand">
      <div class="brand__circle"></div>
      <div class="brand__name">Harbor Lantern IT</div>
    </div>
  </section>

  <section class="card card--back" aria-label="Card back">
    <div class="contact">
      <h1 class="contact__name">ROSS TAVENER</h1>
      <div class="contact__title">Founder, CEO</div>
      <div class="contact__rule contact__rule--top"></div>
      <dl class="phones">
        <dt>OFFICE</dt><dd>209.555.0137</dd>
        <dt>DIRECT</dt><dd>209.555.0182</dd>
        <dt>CELL</dt><dd>209.555.0164</dd>
      </dl>
      <div class="contact__rule contact__rule--bottom"></div>
      <div class="contact__line contact__line--email"><span class="label">EMAIL</span>rtavener@hlit-example.com</div>
      <div class="contact__line contact__line--address">7318 Quillby Avenue Suite F Modesto, CA 95871</div>
      <div class="contact__line contact__line--web">www.hlit-example.com</div>
    </div>
  </section>
</main>
</body>
</html>
```